Business card design for Velvet Harbor

We need business cards designed for our new marketing consulting company, Velvet Harbor. Our services include marketing strategy, go-to-market and launch planning, growth strategy, and execution. We serve medical technology and health technology companies, from startups to well-established growth companies.

The business cards should feel professional, credible, reliable and trustworthy, and should instill confidence. Also bold, creative, and modern.

The design must use the Velvet Harbor logo.

The primary brand color is this orange: #FF5501
A secondary color that you can use is this gray: #282B2D
I would prefer only to use the orange and gray. But if you feel you really need an additional accent color (please use it very sparingly, as little as possible), you can use this blue for small accent purposes: #009FED

Attached are the logo files. The main logo is the one with a little bit of orange on the left and the rest is gray.

The business card should include the following:

Velvet Harbor logo
First name and last name
Title
Email address
Phone number and type (in whatever order looks best for the design
Website (the website does not need to be in the same block as the personal info)

For example:

Nessa Pryle
Founder & Principal
nessa@velvetharbor.com
+1.628.309.4156 mobile (can use "." or spaces in between blocks of numbers)
velvetharbor.com (somewhere on the card, it does not need to be with the personal info; and note that there is no "www." at the beginning)

Note that there will be no address listed on the business card.

Target Market(s)

Executives (CEO, head of marketing, head of sales) at medical technology and health technology companies, mostly in their 40s and older, well-educated, often with advanced degrees. They are strategic thinkers, responsible for budgets, and familiar with P&L. Their comfort with and trust in using outside consultants varies.

Industry/Entity Type

Medical technology and health technology companies.

Contact Information for Business Card

See project description

Font styles to use
Sans Serif

Requirements
Must have
• Logo and see Business card details section above.

```html
<!DOCTYPE html>
<html lang="en">
<head>
<meta charset="utf-8">
<title>Velvet Harbor — Business Card</title>
<link href="https://fonts.googleapis.com/css2?family=Lato:ital,wght@0,400;0,700;1,900&display=swap" rel="stylesheet">
<style>
  :root {
    --orange: #EA5A1E;
    --graphite: #282B2D;
    --paper: #FFFFFF;
    --stage: #3C3F42;
  }
  * { margin: 0; padding: 0; box-sizing: border-box; }
  html, body {
    width: 1200px; height: 1200px; overflow: hidden;
    background: var(--stage);
    font-family: "Lato", Arial, sans-serif;
    color: var(--graphite);
  }
  .card {
    position: absolute;
    left: 162px;
    width: 875px;
    height: 512px;
    background: var(--paper);
    overflow: hidden;
  }
  .card--front { top: 76px; }
  .card--back { top: 617px; }

  .wordmark {
    position: absolute;
    display: flex;
    align-items: center;
    gap: 22px;
  }
  .wordmark__dot {
    border-radius: 50%;
    background: var(--orange);
    flex: none;
  }
  .wordmark__name {
    font-weight: 700;
    text-transform: uppercase;
    color: var(--graphite);
    line-height: 1.05;
  }
  .card--front .wordmark { left: 0; right: 0; top: 72px; justify-content: center; }
  .card--front .wordmark__dot { width: 26px; height: 26px; }
  .card--front .wordmark__name { font-size: 50px; letter-spacing: 12px; }

  .card--back .wordmark { left: 0; right: 0; top: 218px; justify-content: center; }
  .card--back .wordmark__dot { width: 20px; height: 20px; }
  .card--back .wordmark__name { font-size: 34px; letter-spacing: 8px; }

  .person { position: absolute; left: 90px; top: 310px; }
  .person__name {
    font-weight: 900; font-style: italic;
    font-size: 36px; letter-spacing: -0.5px;
    color: var(--orange); text-transform: uppercase;
    line-height: 1;
  }
  .person__title { margin-top: 12px; font-size: 21px; font-weight: 400; }

  .contact {
    position: absolute; right: 86px; top: 314px;
    list-style: none; text-align: right;
  }
  .contact__item {
    display: flex; align-items: center; justify-content: flex-end;
    gap: 24px; font-size: 21px; height: 33px;
  }
  .icon { width: 16px; height: 16px; flex: none; }

  .web-band {
    position: absolute; left: 90px; right: 0; top: 423px; height: 37px;
    background: var(--orange); color: var(--paper);
    display: flex; align-items: center; justify-content: flex-end;
    gap: 24px; padding-right: 86px; font-size: 21px;
  }
</style>
</head>
<body>
  <section class="card card--front">
    <div class="wordmark">
      <span class="wordmark__dot"></span>
      <span class="wordmark__name">Velvet<br>Harbor</span>
    </div>

    <div class="person">
      <h1 class="person__name">Nessa Pryle</h1>
      <p class="person__title">Founder &amp; Principal</p>
    </div>

    <ul class="contact">
      <li class="contact__item">
        <span>+1.628.309.4156</span>
        <svg class="icon" viewBox="0 0 16 16" aria-label="mobile"><rect x="3.5" y="1" width="9" height="14" rx="1.5" fill="none" stroke="#282B2D" stroke-width="1.6"/><rect x="6.5" y="12" width="3" height="1.2" fill="#282B2D"/></svg>
      </li>
      <li class="contact__item">
        <span>nessa@velvetharbor.com</span>
        <svg class="icon" viewBox="0 0 16 16" aria-label="email"><rect x="1" y="3" width="14" height="10" rx="1" fill="#282B2D"/><path d="M1.5 4 L8 9 L14.5 4" fill="none" stroke="#fff" stroke-width="1.3"/></svg>
      </li>
    </ul>

    <div class="web-band">
      <span>velvetharbor.com</span>
      <svg class="icon" viewBox="0 0 16 16" aria-label="website"><circle cx="8" cy="8" r="6.5" fill="none" stroke="#fff" stroke-width="1.5"/><ellipse cx="8" cy="8" rx="2.8" ry="6.5" fill="none" stroke="#fff" stroke-width="1.2"/><line x1="1.5" y1="8" x2="14.5" y2="8" stroke="#fff" stroke-width="1.2"/></svg>
    </div>
  </section>

  <section class="card card--back">
    <div class="wordmark">
      <span class="wordmark__dot"></span>
      <span class="wordmark__name">Velvet<br>Harbor</span>
    </div>
  </section>
</body>
</html>
```